Business cards — need something that creates “wow” factor

Need a sleek and clean looking business card. Something that is clear and consise. These business cards are for my painting business and hundreds will be placed in the Dallas area between all Halverd Pemberton paint stored. These card really need to stick out! Open to any and all ideas...

Target Market(s)

Residential clientele

Industry/Entity Type

Painting

Contact Information for Business Card

Dorian Vakelby
Owner

382.516.2074

Web: Mesahuepainting.example (still under construction)
Mesahuepainting@mailbox.example

Font styles to use
Sans Serif

Colors

Designer to choose colors to be used in the design.

Requirements
Must have
• My name, number, website, email, Socialpage
• and “100% customer satisfaction guaranteed”
• Socialpage.example/Mesahuepainting/
Nice to have
• Listed services
• Interior/exterior painting
• Drywall repair/texture
• Fence staining/refinishing
• Concrete staining
• Epoxy flooring
• Pressure washing

```html
<!DOCTYPE html>
<html lang="en">
<head>
<meta charset="utf-8">
<title>Mesa Hue Painting — Business Card</title>
<link rel="stylesheet" href="https://fonts.googleapis.com/css2?family=Open+Sans:ital,wght@0,400;0,600;1,700&family=Oswald:wght@500&display=swap">
<style>
  :root {
    --page: #3a3a3a;
    --card-back: #e9e9e9;
    --ink: #1e1e1e;
    --accent: #e8412c;
    --white: #ffffff;
    --spec-green: #7cc242;
    --spec-teal: #3aa6b9;
    --spec-purple: #6a3f9a;
    --spec-magenta: #b8257e;
    --spec-orange: #f6a623;
    --spec-red: #d9302c;
  }
  * { box-sizing: border-box; margin: 0; padding: 0; }
  html, body { width: 898px; height: 1200px; overflow: hidden; }
  body { background: var(--page); font-family: "Open Sans", sans-serif; position: relative; }

  .card { position: absolute; left: 140px; width: 616px; height: 354px; overflow: hidden; }
  .card--front { top: 206px; }
  .card--back { top: 644px; background: var(--card-back); }

  .hero-art {
    position: absolute; inset: 0;
    background:
      radial-gradient(circle at 45% 55%, rgba(255,255,255,0.25), rgba(255,255,255,0) 40%),
      conic-gradient(from 200deg at 45% 55%,
        var(--spec-teal), var(--spec-green), #c8d94a, var(--spec-orange),
        var(--spec-red), var(--spec-magenta), var(--spec-purple), #4a5aa8, var(--spec-teal));
  }
  .services-line {
    position: absolute; left: 29px; top: 300px;
    color: var(--white); font-size: 19px; font-weight: 400; letter-spacing: 0.2px;
  }

  .brand { position: absolute; left: 44px; top: 100px; width: 190px; text-align: center; }
  .brand__mark { width: 22px; height: 22px; border-radius: 50%; background: var(--accent); margin: 0 auto 8px; }
  .brand__name { font-size: 38px; font-weight: 600; color: var(--ink); line-height: 1; letter-spacing: 1px; }
  .brand__tagline { font-size: 9px; color: var(--ink); margin-top: 8px; }

  .owner { position: absolute; right: 40px; top: 40px; text-align: right; }
  .owner__name { font-size: 26px; font-weight: 400; color: var(--ink); line-height: 1.1; }
  .owner__title-row { display: flex; align-items: center; gap: 10px; justify-content: flex-end; margin-top: 2px; }
  .owner__rule { width: 120px; height: 2px; background: var(--accent); }
  .owner__title { font-size: 20px; font-weight: 700; font-style: italic; color: var(--accent); letter-spacing: 2px; }

  .contact-list { position: absolute; left: 300px; top: 130px; list-style: none; }
  .contact-list li { display: flex; align-items: center; gap: 10px; height: 34px; font-size: 15.5px; color: var(--ink); }
  .contact-icon { width: 22px; height: 22px; flex: none; }

  .guarantee-band {
    position: absolute; left: 49px; width: 518px; bottom: 0; height: 50px;
    background: var(--accent); border-radius: 16px 16px 0 0;
    display: flex; align-items: center; justify-content: center;
    font-family: "Oswald", sans-serif; font-weight: 500; font-size: 23px;
    letter-spacing: 2.5px; color: var(--white); text-transform: uppercase;
  }
</style>
</head>
<body>

<section class="card card--front">
  <div class="hero-art" role="img" aria-label="Rainbow colour-wheel sunburst with a painter in a white shirt rolling paint on a long pole"></div>
  <p class="services-line">Commercial | Residential &nbsp;| Interior | Exterior</p>
</section>

<section class="card card--back">
  <div class="brand">
    <div class="brand__mark"></div>
    <div class="brand__name">Mesa Hue</div>
    <div class="brand__tagline">Commercial | Residential | Interior | Exterior</div>
  </div>

  <div class="owner">
    <div class="owner__name">Dorian Vakelby</div>
    <div class="owner__title-row">
      <span class="owner__rule"></span>
      <span class="owner__title">Owner</span>
    </div>
  </div>

  <ul class="contact-list">
    <li>
      <svg class="contact-icon" viewBox="0 0 22 22" aria-hidden="true"><circle cx="11" cy="11" r="11" fill="var(--accent)"/><path d="M7.5 6h2l1 2.5-1.3 1a6 6 0 0 0 3.3 3.3l1-1.3 2.5 1v2a1 1 0 0 1-1 1A9 9 0 0 1 6.5 7a1 1 0 0 1 1-1z" fill="#fff"/></svg>
      382.516.2074
    </li>
    <li>
      <svg class="contact-icon" viewBox="0 0 22 22" aria-hidden="true"><circle cx="11" cy="11" r="11" fill="var(--accent)"/><g fill="none" stroke="#fff" stroke-width="1.3"><circle cx="11" cy="11" r="6"/><ellipse cx="11" cy="11" rx="2.6" ry="6"/><path d="M5 11h12M6 8h10M6 14h10"/></g></svg>
      www.mesahuepainting.example
    </li>
    <li>
      <svg class="contact-icon" viewBox="0 0 22 22" aria-hidden="true"><text x="11" y="17" text-anchor="middle" font-family="Open Sans, sans-serif" font-size="20" font-weight="600" fill="var(--accent)">@</text></svg>
      mesahuepainting@mailbox.example
    </li>
    <li>
      <svg class="contact-icon" viewBox="0 0 22 22" aria-hidden="true"><circle cx="11" cy="11" r="11" fill="var(--accent)"/></svg>
      Socialpage.example/Mesahuepainting
    </li>
  </ul>

  <div class="guarantee-band">100% Customer Satisfaction Guaranteed</div>
</section>

</body>
</html>
```